Elevating our current Business Card Design

We want to elevate our current business card with a new design to look like a marlow 800 company. We are a premium lubricant distributor (oil and grease).
We need 2 versions, version 1 is as per the uploaded a copy of our current business card with the English version.
For our Chinese version we need to use the front to be English in English and have the back of the card designed exactly like the front for all info to be in Chinese.
The design template needs to be such that we can amend the template with adding different information for each person's card.
The background colour of the card can be changed- we just need to clearly see all information on the card and logos.
The TRV and Verdant Mark logos cannot have any colour or display changes- only use the logos attached.
All logos need to be included and all information from the attached current card

```html
<!DOCTYPE html>
<html lang="en">
<head>
<meta charset="utf-8">
<title>Corvane Lubricant Distributors – Business Card</title>
<link rel="stylesheet" href="https://fonts.googleapis.com/css2?family=Montserrat:wght@400;500;600;800&display=swap">
<style>
  :root{
    --stage:#2b2b2b;
    --card:#ffffff;
    --panel:#efefef;
    --red:#e5261f;
    --ink:#333333;
    --grey:#8a8a8a;
    --orange:#ef7d22;
    --green:#1f5a3a;
  }
  *{margin:0;padding:0;box-sizing:border-box}
  html,body{width:1200px;height:800px;overflow:hidden;background:var(--stage);font-family:"Montserrat",sans-serif}
  .stage{position:relative;width:1200px;height:800px}
  .card{position:absolute;width:595px;height:340px;background:var(--card);overflow:hidden;box-shadow:0 10px 30px rgba(0,0,0,.45)}
  .card--front{left:302px;top:40px}
  .card--back{left:302px;top:420px}

  /* front */
  .accent{position:absolute;height:9px;width:58px;background:var(--red)}
  .accent--top{right:0;top:22px}
  .accent--bottom{left:0;bottom:22px}
  .front-brand{position:absolute;left:0;right:0;top:92px;display:flex;flex-direction:column;align-items:center;gap:26px}
  .wordmark{display:flex;align-items:center;gap:14px}
  .wordmark-dot{width:30px;height:30px;border-radius:50%;background:var(--orange)}
  .wordmark-name{font-weight:800;font-size:64px;color:var(--red);letter-spacing:2px;line-height:1}
  .front-title{font-weight:500;font-size:18px;letter-spacing:1.6px;color:var(--red);text-transform:uppercase}

  /* back */
  .back-art{position:absolute;inset:0}
  .brand-box{position:absolute;left:22px;top:104px;width:128px;height:40px;border:1.5px solid var(--red);border-radius:5px;display:flex;align-items:center;gap:6px;padding:0 8px}
  .brand-box-dot{width:9px;height:9px;border-radius:50%;background:var(--orange);flex:none}
  .brand-box-name{font-weight:600;font-size:8px;line-height:1.15;color:var(--red);text-transform:uppercase}
  .partner{position:absolute;left:150px;top:104px;width:112px;height:40px;background:var(--red);display:flex;flex-direction:column;justify-content:center;padding-left:12px;color:#fff;font-weight:600;text-transform:uppercase}
  .partner-name{font-size:15px;letter-spacing:.5px;line-height:1}
  .partner-sub{font-size:6.5px;letter-spacing:.4px;margin-top:3px}
  .cert{position:absolute;top:72px;width:40px;height:40px;border-radius:50%;background:var(--orange);border:4px solid #c9c9c9}
  .cert--1{left:282px}
  .cert--2{left:352px}
  .cert--3{left:422px}
  .member-badge{position:absolute;left:500px;top:30px;width:56px;height:40px;border-radius:28px 28px 6px 6px;background:var(--green)}

  .contacts{position:absolute;left:38px;top:184px;list-style:none;display:flex;flex-direction:column;gap:7px}
  .contacts li{display:flex;align-items:center;gap:12px;font-size:14px;color:var(--ink);letter-spacing:.3px}
  .contacts svg{width:14px;height:14px;flex:none}
  .divider{position:absolute;left:350px;top:178px;width:1.5px;height:130px;background:var(--red)}
  .person{position:absolute;left:374px;top:172px}
  .person-name{font-weight:800;font-size:20px;color:var(--ink);letter-spacing:.6px;text-transform:uppercase}
  .person-role{font-size:14px;color:var(--ink);margin-top:2px}
  .person-address{margin-top:38px;font-size:14px;color:var(--ink);line-height:1.35;font-style:normal}
</style>
</head>
<body>
<main class="stage">

  <section class="card card--front" aria-label="Card front">
    <span class="accent accent--top"></span>
    <span class="accent accent--bottom"></span>
    <div class="front-brand">
      <div class="wordmark">
        <span class="wordmark-dot"></span>
        <span class="wordmark-name">CLD</span>
      </div>
      <p class="front-title">Corvane Lubricant Distributors</p>
    </div>
  </section>

  <section class="card card--back" aria-label="Card back">
    <svg class="back-art" viewBox="0 0 595 340" width="595" height="340">
      <polygon points="0,152 348,152 364,136 500,136 516,120 595,0 595,340 0,340" fill="var(--panel)"/>
      <polyline points="0,152 348,152 364,136 500,136 516,120 595,0" fill="none" stroke="var(--red)" stroke-width="1.5"/>
    </svg>

    <div class="brand-box">
      <span class="brand-box-dot"></span>
      <span class="brand-box-name">Corvane<br>Lubricant<br>Distributors</span>
    </div>
    <div class="partner">
      <span class="partner-name">Kestrel</span>
      <span class="partner-sub">Premium Lubricants</span>
    </div>
    <span class="cert cert--1" role="img" aria-label="TRV certification badge"></span>
    <span class="cert cert--2" role="img" aria-label="TRV certification badge"></span>
    <span class="cert cert--3" role="img" aria-label="TRV certification badge"></span>
    <span class="member-badge" role="img" aria-label="Verdant Mark network member badge"></span>

    <ul class="contacts">
      <li><svg viewBox="0 0 24 24"><path fill="var(--red)" d="M6.6 10.8a15 15 0 0 0 6.6 6.6l2.2-2.2c.3-.3.7-.4 1-.2 1.1.4 2.3.6 3.6.6.6 0 1 .4 1 1V20c0 .6-.4 1-1 1A17 17 0 0 1 3 4c0-.6.4-1 1-1h3.5c.6 0 1 .4 1 1 0 1.3.2 2.5.6 3.6.1.3 0 .7-.2 1z"/></svg>1300 472 615</li>
      <li><svg viewBox="0 0 24 24"><rect x="5" y="2" width="14" height="20" rx="2" fill="none" stroke="var(--red)" stroke-width="2"/><circle cx="12" cy="18" r="1.3" fill="var(--red)"/></svg>+61 412 908 336</li>
      <li><svg viewBox="0 0 24 24"><rect x="3" y="9" width="18" height="12" rx="2" fill="var(--red)"/><rect x="7" y="3" width="10" height="7" fill="none" stroke="var(--red)" stroke-width="2"/></svg>+61 8 9270 4418</li>
      <li><svg viewBox="0 0 24 24"><rect x="2" y="5" width="20" height="14" rx="1" fill="var(--red)"/><polyline points="2,6 12,13 22,6" fill="none" stroke="#fff" stroke-width="1.6"/></svg>dana.whitlow@corvanedirect.com</li>
      <li><svg viewBox="0 0 24 24"><circle cx="12" cy="12" r="9" fill="none" stroke="var(--red)" stroke-width="2"/><ellipse cx="12" cy="12" rx="4" ry="9" fill="none" stroke="var(--red)" stroke-width="1.6"/><line x1="3" y1="12" x2="21" y2="12" stroke="var(--red)" stroke-width="1.6"/></svg>www.corvanedirect.com</li>
    </ul>

    <span class="divider"></span>

    <div class="person">
      <h1 class="person-name">Dana Whitlow</h1>
      <p class="person-role">Administration Executive</p>
      <address class="person-address">48 Depot Crescent<br>Ashvale, WA 6110</address>
    </div>
  </section>

</main>
</body>
</html>
```